looking to design ads for a calendar.

We have the copy and brand assets created and ready to go. We need 1 large design for the front of the calendar and inside of the calendar. The specs are:

First interior page: 5 inches by 7.5 inches
Month pages (14 in total): 2.5 inches by 7.5 inches
PDF preferred, high resolution

```html
<!DOCTYPE html>
<html lang="en">
<head>
<meta charset="utf-8">
<title>Counties in Focus – March 2025</title>
<link rel="stylesheet" href="https://fonts.googleapis.com/css2?family=Oswald:wght@400;500&family=Roboto:wght@400;700;900&display=swap">
<style>
  :root {
    --brown: #8b714c;
    --green: #1b5444;
    --red: #a3202a;
    --ink: #111111;
    --rule: #c9c9c9;
    --paper: #ffffff;
  }
  * { box-sizing: border-box; margin: 0; padding: 0; }
  html, body { width: 800px; height: 1200px; overflow: hidden; background: var(--paper); }
  .page { position: relative; width: 800px; height: 1200px; overflow: hidden; background: var(--paper); font-family: "Roboto", Arial, sans-serif; }
  .frame { position: absolute; inset: 0; width: 800px; height: 1200px; }
  .frame path { fill: var(--brown); }

  .brand { position: absolute; left: 90px; top: 90px; width: 230px; display: flex; align-items: center; gap: 14px; }
  .brand-dot { flex: none; width: 34px; height: 34px; border-radius: 50%; background: var(--green); }
  .brand-name { font-weight: 700; font-size: 26px; line-height: 1.15; color: var(--green); }

  .year { position: absolute; right: 62px; top: 62px; font-weight: 900; font-size: 92px; line-height: 1; color: var(--brown); letter-spacing: 1px; }
  .series { position: absolute; left: 333px; top: 174px; width: 405px; height: 36px; background: var(--green); clip-path: polygon(28px 0, 100% 0, 100% 100%, 0 100%); color: #fff; font-size: 25px; letter-spacing: 1.5px; text-align: right; padding-right: 14px; line-height: 36px; }
  .month { position: absolute; right: 60px; top: 218px; font-weight: 900; font-size: 54px; letter-spacing: 6px; color: var(--green); line-height: 1; }

  .calendar { position: absolute; left: 61px; top: 327px; width: 677px; }
  .weekdays { display: grid; grid-template-columns: repeat(7, 1fr); gap: 0; }
  .weekday { margin: 0 8px; height: 38px; background: var(--green); color: #fff; font-weight: 700; font-size: 22px; text-align: center; line-height: 38px; border-radius: 16px 2px 16px 2px; }
  .days { display: grid; grid-template-columns: repeat(7, 1fr); grid-auto-rows: 97px; }
  .day { font-family: "Oswald", "Arial Narrow", sans-serif; font-size: 46px; color: var(--ink); text-align: center; line-height: 90px; border-right: 1px solid var(--rule); border-bottom: 1px solid var(--rule); }
  .day:nth-child(7n) { border-right: none; }
  .day.sunday { color: var(--red); }
  .days .day.last-row { border-bottom: none; }

  .theme { position: absolute; left: 61px; top: 872px; font-size: 20px; color: var(--ink); }
  .theme strong { font-size: 24px; font-weight: 700; color: var(--green); }

  .note { position: absolute; left: 61px; top: 1009px; width: 682px; height: 147px; border: 2px solid var(--green); border-radius: 18px; overflow: hidden; }
  .note-label { position: absolute; left: 0; top: 0; width: 324px; height: 32px; background: var(--green); clip-path: polygon(0 0, 100% 0, 88% 100%, 0 100%); color: #fff; font-size: 23px; line-height: 32px; padding-left: 92px; }
  .note-text { position: absolute; left: 18px; right: 18px; top: 44px; font-size: 19px; line-height: 1.4; color: var(--ink); text-align: justify; }
</style>
</head>
<body>
<div class="page">
  <svg class="frame" viewBox="0 0 750 1125" aria-hidden="true">
    <path d="M0 0 H490 Q478 18 445 18 H20 V900 L0 922 Z"/>
    <path d="M750 205 V1125 H258 Q278 1108 312 1108 H735 V232 Q735 214 750 205 Z"/>
  </svg>

  <div class="brand">
    <span class="brand-dot"></span>
    <span class="brand-name">Statewide Counties Guild</span>
  </div>

  <div class="year">2025</div>
  <div class="series">Counties in Focus</div>
  <h1 class="month">MARCH</h1>

  <div class="calendar">
    <div class="weekdays">
      <div class="weekday">S</div><div class="weekday">M</div><div class="weekday">T</div><div class="weekday">W</div><div class="weekday">T</div><div class="weekday">F</div><div class="weekday">S</div>
    </div>
    <div class="days">
      <div class="day sunday">1</div><div class="day">2</div><div class="day">3</div><div class="day">4</div><div class="day">5</div><div class="day">6</div><div class="day">7</div>
      <div class="day sunday">8</div><div class="day">9</div><div class="day">10</div><div class="day">11</div><div class="day">12</div><div class="day">13</div><div class="day">14</div>
      <div class="day sunday">15</div><div class="day">16</div><div class="day">17</div><div class="day">18</div><div class="day">19</div><div class="day">20</div><div class="day">21</div>
      <div class="day sunday">22</div><div class="day">23</div><div class="day">24</div><div class="day">25</div><div class="day">26</div><div class="day">27</div><div class="day">28</div>
      <div class="day sunday last-row">29</div><div class="day last-row">30</div><div class="day last-row">31</div><div class="day last-row"></div><div class="day last-row"></div><div class="day last-row"></div><div class="day last-row"></div>
    </div>
  </div>

  <p class="theme">March 1950s : <strong>Post-war growth.</strong></p>

  <div class="note">
    <div class="note-label">Subhead:</div>
    <p class="note-text">As counties expanded, so did financial responsibilities. With FundWise, your team can do more with what you already have</p>
  </div>
</div>
</body>
</html>
```